DOVR Business Card Design Project

Company Name: DOVR (Dove Operational Versatile Resources) JLT.
Office Address: Office No 218, Saffron Crest Tower, Palmera Bay Towers, Dubai, U.A.E
Company line of business:
1) Currently we have a POS solution for retail outlets like duty free shops, supermarkets, department stores etc... The solution is deployed in Harbor Gate Retail on 350 POS and in Coralline Port Retail on 100 POS. So our main line of business is the deployment of this solution in retail outlets locally or regionally. We have already deployed the solution in India and Australia.
2) Integration of other third party POS systems with an online credit authorization netwotk in the UAE. This will enable POS applications to connect directly to the acquiring banks without needing an EFT terminal like Paxoline or Tramodex. The credit card payment is completed at the POS.
3) Other solutions that are targeting retail outlets like mobile POS, queue busting solutions, stock taking solutions using hand held devices, transaction capture systems, etc...
4) Other IT services like support of call center solutions from Bramwell Systems and development of new solutions as per customer requirements.
We need a business card design for the company. We don't have any specific requirements and will eave up to the designers to come up with creative designs. At the moment we still don't have a letter head design and the only thing that we have is the company logo that we will upload shortly.
Updates
Dear All,
I just uploaded the logo source files. I am sorry for the delay.
Regards
Tarek Demirci
I would like the business cards to have the following details:
Company Tel No
Company Fax No
Company Website Address
Employee Name
Employee Title
Employee Mobile Number
Employee Email Address

```html
<!DOCTYPE html>
<html lang="en">
<head>
<meta charset="utf-8">
<title>DOVR Business Card</title>
<link rel="stylesheet" href="https://fonts.googleapis.com/css2?family=Source+Sans+3:wght@400;600&display=swap">
<style>
  :root {
    --backdrop: #e9e7e4;
    --card-white: #ffffff;
    --ink-dark: #231f20;
    --ink-grey: #555555;
    --ink-light: #ffffff;
    --brand-red: #ed1c24;
    --brand-red-deep: #b3141b;
    --brand-blue: #0a8fd8;
    --brand-blue-deep: #0a5aa8;
  }
  * { margin: 0; padding: 0; box-sizing: border-box; }
  html, body {
    width: 1200px; height: 390px; overflow: hidden;
    background: var(--backdrop);
    font-family: "Source Sans 3", "Myriad Pro", sans-serif;
  }
  .canvas { position: relative; width: 1200px; height: 390px; }
  .card {
    position: absolute; top: 43px;
    width: 528px; height: 304px;
    background: var(--card-white);
    overflow: hidden;
    box-shadow: 0 2px 8px rgba(0,0,0,0.18);
  }
  .card--front { left: 40px; }
  .card--back { left: 632px; }
  .card__swoosh { position: absolute; inset: 0; width: 100%; height: 100%; }
  .brand {
    position: absolute; left: 118px; top: 58px;
    display: flex; align-items: center; gap: 22px;
  }
  .brand__dot {
    width: 46px; height: 46px; border-radius: 50%;
    background: var(--brand-red);
  }
  .brand__name {
    font-size: 72px; font-weight: 400; line-height: 1;
    color: var(--ink-dark); letter-spacing: 1px;
  }
  .person {
    position: absolute; left: 34px; top: 172px;
    font-size: 17px; color: var(--ink-grey);
  }
  .person__name { font-weight: 600; }
  .person__title { font-size: 14px; }
  .address {
    position: absolute; left: 34px; top: 218px;
    font-size: 13.5px; line-height: 18px; color: var(--ink-grey);
    font-style: normal;
  }
  .contacts {
    position: absolute; right: 22px; top: 201px;
    list-style: none; color: var(--ink-light);
    font-size: 13.5px; line-height: 18px; text-align: right;
  }
  .contacts li { display: flex; justify-content: flex-end; align-items: center; gap: 8px; }
  .contacts svg { width: 11px; height: 11px; fill: var(--ink-light); }
</style>
</head>
<body>
<div class="canvas">

  <section class="card card--front">
    <svg class="card__swoosh" viewBox="0 0 528 304" aria-hidden="true">
      <defs>
        <linearGradient id="blueBand" x1="0" y1="0" x2="0.3" y2="1">
          <stop offset="0" stop-color="var(--brand-blue)"/>
          <stop offset="1" stop-color="var(--brand-blue-deep)"/>
        </linearGradient>
        <radialGradient id="redField" cx="0.35" cy="0.75" r="0.6">
          <stop offset="0" stop-color="var(--brand-red-deep)"/>
          <stop offset="1" stop-color="var(--brand-red)"/>
        </radialGradient>
      </defs>
      <path d="M452,0 L528,0 L528,304 L168,304 C320,262 448,168 452,0 Z" fill="url(#blueBand)"/>
      <path d="M528,72 C498,190 380,272 212,304 L528,304 Z" fill="url(#redField)"/>
    </svg>

    <div class="brand">
      <span class="brand__dot"></span>
      <span class="brand__name">DOVR</span>
    </div>

    <p class="person"><span class="person__name">Name</span> / <span class="person__title">Title</span></p>

    <address class="address">
      Office No 218,<br>
      Saffron Crest Tower,<br>
      Palmera Bay Towers,<br>
      Dubai, U.A.E
    </address>

    <ul class="contacts">
      <li>123-456-7890
        <svg viewBox="0 0 12 12"><path d="M3 1 L5 3.5 L4 5 C5 7 6 8 7 8.5 L8.5 7.5 L11 9.5 L9.5 11 C5 10.5 1.5 7 1 2.5 Z"/></svg></li>
      <li>123-456-7890
        <svg viewBox="0 0 12 12"><path d="M3.5 0.5 H8.5 V11.5 H3.5 Z M4.5 1.5 V8.5 H7.5 V1.5 Z"/></svg></li>
      <li>123-456-7890
        <svg viewBox="0 0 12 12"><path d="M3 1 H9 V4 H11 V9 H9 V11 H3 V9 H1 V4 H3 Z M4 2 V4 H8 V2 Z M4 8 V10 H8 V8 Z"/></svg></li>
      <li>www.website.com
        <svg viewBox="0 0 12 12"><path d="M6 0.5 A5.5 5.5 0 1 0 6.01 0.5 Z M6 1.5 C7.5 3 7.5 9 6 10.5 C4.5 9 4.5 3 6 1.5 Z M1.5 5.5 H10.5 V6.5 H1.5 Z" fill-rule="evenodd"/></svg></li>
      <li>dovr@email.com
        <svg viewBox="0 0 12 12"><path d="M6 0.5 A5.5 5.5 0 1 0 10 9.5 L9.3 8.8 A4.5 4.5 0 1 1 10.5 6 V7 C10.5 8 9 8 9 7 V3.5 H8 V4 A2.5 2.5 0 1 0 8 8 C8.8 9.3 11.5 9 11.5 7 V6 A5.5 5.5 0 0 0 6 0.5 Z M6 4.5 A1.5 1.5 0 1 1 5.99 4.5 Z" fill-rule="evenodd"/></svg></li>
    </ul>
  </section>

  <section class="card card--back">
    <svg class="card__swoosh" viewBox="0 0 528 304" aria-hidden="true">
      <defs>
        <linearGradient id="blueBandBack" x1="0" y1="0" x2="0.3" y2="1">
          <stop offset="0" stop-color="var(--brand-blue)"/>
          <stop offset="1" stop-color="var(--brand-blue-deep)"/>
        </linearGradient>
        <radialGradient id="redFieldBack" cx="0.35" cy="0.75" r="0.6">
          <stop offset="0" stop-color="var(--brand-red-deep)"/>
          <stop offset="1" stop-color="var(--brand-red)"/>
        </radialGradient>
      </defs>
      <path d="M452,0 L528,0 L528,304 L168,304 C320,262 448,168 452,0 Z" fill="url(#blueBandBack)"/>
      <path d="M528,72 C498,190 380,272 212,304 L528,304 Z" fill="url(#redFieldBack)"/>
      <circle cx="438" cy="236" r="42" fill="#ffffff" fill-opacity="0.12"/>
    </svg>

    <div class="brand">
      <span class="brand__dot"></span>
      <span class="brand__name">DOVR</span>
    </div>
  </section>

</div>
</body>
</html>
```